Designing A poster for a zany musical comedy slated for an Off-Broadway run!

We need a poster design for a musical comedy that is scheduled in theatres around the U.S. The poster needs to capture the audacious and crazy nature of this cutting edge musical where 7 actors play everyone in the town, men, women and children. The show is funny, political, satirical, absurd and controversial.
Synopsis:A new campy, cheeky, audacious musical comedy. The ladies of the Pellbrook Third Gospel Chapel Ladies’ Helping Circle are getting together to produce their annual Harvest Bonnet Jubilee. Six actors play every character in this singing, acting, dancing, improv tour de force. As the ‘Steeple Belles’ prepare for their pageant, chaos and calamity bring out less than ‘saintly’ behavior. The result is Heaven sent hilarity!

A review to give you an idea: “It’s hoot. Actually, that is too mild a word. At its heart, this is a showcase for six journeymen actors (and one musician) to strut their prodigious talents…The result is like the funnyman’s version of an TVSN highlight reel – nonstop humor from first-rate pros. When they turn their attention to the serious business of humor – to primping and eyelash-batting, to hip-wiggling, to catty banter, to the deliciously clever maze of men playing women who are mocking men – it’s a ball.”—Review by Walter Prisk, Dayfield Courier, 2010--

Target Market(s)

Broadway and Theatre audiences

Industry/Entity Type

Entertainment Industry

Logo Text

STEEPLE BELLES, the musical

Colors

Designer to choose colors to be used in the design.

Requirements
Must have
• It must have the title: STEEPLE BELLES
• It should the subtitle: The Musical
• It must have the following credits:
• Book and Story by Rob Haskett
• Music by Corey Blandt, Lyrics by Maureen Haskett
• Additional Material by Winfield Parrow
Nice to have
• It should have a sense of humor. Attached are images of the characters in the town of Pellbrook, U.S.A. Use these images if you like. Not the photographic image but maybe caricatures of the images. Maybe cartoon or stylized?
• It should have a sense of humor. Attached are images of the characters in the town of Pellbrook, U.S.A. Use these images to create caricatures. Not the photographic image but maybe caricatures of the images. Maybe cartoon or stylized? Or perhaps stay away from people and feature a church... with a toppled steeple... or a tilted steeple. Or maybe the characters peeking out through the windows of the church...
Should not have
• Do not use the photographs. Instead more graphic designed or illustrated.The photographs provided are just for reference. Do not put these in the design! You can use them to create caricatures or cartoon versions of the people. But do not just cut and paste the photos. Instead more graphic designed or illustrated.

```html
<!DOCTYPE html>
<html lang="en">
<head>
<meta charset="utf-8">
<title>Steeple Belles – the Musical</title>
<link rel="stylesheet" href="https://fonts.googleapis.com/css2?family=Advent+Pro:wght@300&family=Mrs+Saint+Delafield&family=Oswald:wght@300;400&display=swap">
<style>
  :root {
    --backdrop: #e9e9e7;
    --paper: #f8e6d6;
    --paper-light: #fbeee3;
    --ink: #3a3533;
    --ink-soft: rgba(58, 53, 51, 0.62);
    --tile-green: #4fb48b;
    --tile-coral: #f47b68;
    --tile-yellow: #fbb84b;
    --tile-orange: #f06424;
    --tile-purple: #9c80b4;
    --tile-pink: #ee3f6f;
    --tile-salmon: #f57a6c;
  }
  * { margin: 0; padding: 0; box-sizing: border-box; }
  html, body {
    width: 1200px; height: 1148px; overflow: hidden;
    background: var(--backdrop);
  }
  .poster {
    position: absolute; left: 190px; top: 24px;
    width: 820px; height: 1100px;
    background: linear-gradient(160deg, var(--paper) 0%, var(--paper-light) 100%);
  }
  .cast-cross { position: absolute; inset: 0; }
  .cast-tile {
    position: absolute; width: 86px; height: 86px;
    background-image: radial-gradient(ellipse 34% 40% at 50% 50%, var(--ink-soft) 0%, var(--ink-soft) 35%, transparent 100%);
  }
  .tile-top    { left: 367px; top: 272px; background-color: var(--tile-green); }
  .tile-left   { left: 261px; top: 378px; background-color: var(--tile-coral); }
  .tile-centre { left: 367px; top: 378px; background-color: var(--tile-yellow); }
  .tile-right  { left: 473px; top: 378px; background-color: var(--tile-orange); }
  .tile-stem-1 { left: 370px; top: 484px; background-color: var(--tile-purple); }
  .tile-stem-2 { left: 374px; top: 590px; background-color: var(--tile-pink); }
  .tile-stem-3 { left: 378px; top: 696px; background-color: var(--tile-salmon); }

  .title-block {
    position: absolute; left: 0; right: 0; top: 0;
    text-align: center; color: var(--ink);
  }
  .show-title {
    position: absolute; left: 0; right: 0; top: 896px;
    font-family: "Advent Pro", sans-serif; font-weight: 300;
    font-size: 56px; letter-spacing: 2px; line-height: 1;
    transform: scaleY(1.7); transform-origin: 50% 0;
  }
  .show-subtitle {
    position: absolute; left: 0; right: 0; top: 990px;
    font-family: "Mrs Saint Delafield", cursive;
    font-size: 30px; line-height: 1; color: #5a514d;
  }
  .credits {
    position: absolute; left: 0; right: 0; top: 1030px;
    font-family: "Oswald", sans-serif; font-weight: 400;
    text-transform: uppercase; color: var(--ink);
    line-height: 1.45;
  }
  .credit-line { font-size: 12px; letter-spacing: 0.1px; }
  .credit-line small { font-size: 8px; font-weight: 300; }
</style>
</head>
<body>
  <main class="poster">
    <div class="cast-cross">
      <div class="cast-tile tile-top" role="img" aria-label="Green tile with a stylised cast member's hair silhouette"></div>
      <div class="cast-tile tile-left" role="img" aria-label="Coral tile with a stylised cast member's hair silhouette"></div>
      <div class="cast-tile tile-centre" role="img" aria-label="Yellow tile with a stylised cast member's hair silhouette"></div>
      <div class="cast-tile tile-right" role="img" aria-label="Orange tile with a stylised cast member's hair silhouette"></div>
      <div class="cast-tile tile-stem-1" role="img" aria-label="Purple tile with a stylised cast member wearing glasses and a halo"></div>
      <div class="cast-tile tile-stem-2" role="img" aria-label="Pink tile with a stylised curly-haired cast member wearing glasses"></div>
      <div class="cast-tile tile-stem-3" role="img" aria-label="Salmon tile with a stylised cast member wearing glasses"></div>
    </div>

    <header class="title-block">
      <h1 class="show-title">STEEPLE BELLES</h1>
      <p class="show-subtitle">the Musical</p>
      <div class="credits">
        <p class="credit-line"><small>Book and story by</small> Rob Haskett <small>music by</small> Corey Blandt, <small>lyrics by</small> Maureen Haskett</p>
        <p class="credit-line"><small>Additional material by</small> Winfield Parrow</p>
      </div>
    </header>
  </main>
</body>
</html>
```